Kick Ass, Edgy, Fun, E commerce Embroidery Company Business Card

Sleek and edgy business card layout. main logo on front with business description (Custom Embroidery, the file is submitted is supposed to look like stitching)
Name, address, phone numbers, social icons (Facebook and Instagram) on back. The card will be black plastic and the front main logo will be printed Spot UV.

Target Market(s)

Small Business Owners

Contact Information for Business Card

Focused, not cluttered and sleek. Modern looking.

Font styles to use
Other font styles liked:
• Very clean and elegant

Colors
acd136

Requirements
Must have
• Custom Embroidery

our Tagline: Every Logo Has A Story - Thread Yours
Nice to have
• Social Icons for Facebook and Instagram
Should not have
• Too much visual noise

```html
<!DOCTYPE html>
<html lang="en">
<head>
<meta charset="utf-8">
<title>Rocco Stitch – Business Card</title>
<link rel="stylesheet" href="https://fonts.googleapis.com/css2?family=Archivo+Black&family=Montserrat:wght@400;600;700;800&display=swap">
<style>
  :root {
    --stage: #5e5e5e;
    --card: #3a3a3c;
    --lime: #acd136;
    --ink: #333335;
    --white: #ffffff;
    --soft: #e9e9e9;
  }
  * { box-sizing: border-box; margin: 0; padding: 0; }
  html, body { width: 1200px; height: 1000px; overflow: hidden; }
  body {
    background: var(--stage);
    font-family: "Montserrat", sans-serif;
    position: relative;
  }
  .card {
    position: absolute;
    top: 190px;
    width: 380px;
    height: 620px;
    background: var(--card);
    overflow: hidden;
    box-shadow: 0 10px 30px rgba(0,0,0,.25);
  }
  .card--front { left: 170px; }
  .card--back { left: 650px; }

  /* front */
  .brand {
    position: absolute;
    left: 0; right: 0; top: 150px;
    text-align: center;
  }
  .brand__dot {
    width: 70px; height: 70px;
    border-radius: 50%;
    background: var(--lime);
    margin: 0 auto 30px;
  }
  .brand__name {
    font-family: "Archivo Black", sans-serif;
    color: var(--white);
    font-size: 62px;
    line-height: 0.95;
    letter-spacing: 1px;
  }
  .service-band {
    position: absolute;
    left: 0; right: 0; top: 430px;
    height: 120px;
    background: var(--lime);
    display: flex; flex-direction: column;
    justify-content: center; align-items: center;
    font-family: "Archivo Black", sans-serif;
    color: var(--ink);
    font-size: 36px;
    line-height: 1;
    letter-spacing: 1px;
  }

  /* back */
  .name-band {
    position: absolute;
    left: 0; right: 0; top: 36px;
    height: 42px;
    background: var(--lime);
    display: flex; align-items: center; justify-content: center;
    font-weight: 700; font-size: 17px;
    letter-spacing: 1.5px;
    color: var(--ink);
    text-transform: uppercase;
  }
  .contact {
    position: absolute;
    left: 46px; top: 116px;
    list-style: none;
  }
  .contact__item {
    display: flex; align-items: center;
    gap: 12px;
    height: 38px;
    color: var(--soft);
    font-size: 17px;
    letter-spacing: .5px;
  }
  .contact__icon { width: 26px; height: 26px; flex: none; }
  .company {
    position: absolute;
    left: 0; right: 0; top: 262px;
    text-align: center;
    color: var(--soft);
    font-size: 17px;
    line-height: 1.35;
  }
  .company__name {
    color: var(--lime);
    font-weight: 700;
    letter-spacing: 1px;
  }
  .social {
    position: absolute;
    left: 0; right: 0; top: 368px;
    display: flex; align-items: center; justify-content: center;
    gap: 12px;
    color: var(--lime);
    font-weight: 600;
    font-size: 17px;
  }
  .social__dot {
    width: 34px; height: 34px;
    border-radius: 50%;
    background: var(--lime);
  }
  .tagline-band {
    position: absolute;
    left: 0; right: 0; top: 450px;
    height: 110px;
    background: var(--lime);
    display: flex; flex-direction: column;
    justify-content: center; align-items: center;
    font-weight: 800;
    font-size: 20px;
    letter-spacing: 1px;
    line-height: 1.35;
    text-transform: uppercase;
  }
  .tagline-band__lead { color: var(--white); }
  .tagline-band__close { color: var(--ink); }
</style>
</head>
<body>

<section class="card card--front" aria-label="Card front">
  <div class="brand">
    <div class="brand__dot"></div>
    <div class="brand__name">ROCCO<br>STITCH</div>
  </div>
  <div class="service-band">
    <span>CUSTOM</span>
    <span>EMBROIDERY</span>
  </div>
</section>

<section class="card card--back" aria-label="Card back">
  <div class="name-band">Dalton Reyes</div>

  <ul class="contact">
    <li class="contact__item">
      <svg class="contact__icon" viewBox="0 0 26 26" fill="none" stroke="var(--lime)" stroke-width="1.6">
        <circle cx="13" cy="13" r="12"/>
        <rect x="9" y="6.5" width="8" height="13" rx="1.2"/>
        <line x1="12" y1="17" x2="14" y2="17"/>
      </svg>
      800 - 555 - 0142
    </li>
    <li class="contact__item">
      <svg class="contact__icon" viewBox="0 0 26 26" fill="none" stroke="var(--lime)" stroke-width="1.6">
        <circle cx="13" cy="13" r="12"/>
        <rect x="6.5" y="8.5" width="13" height="9" rx="1"/>
        <polyline points="6.5,8.5 13,14 19.5,8.5"/>
      </svg>
      info@roccostitch.com
    </li>
    <li class="contact__item">
      <svg class="contact__icon" viewBox="0 0 26 26" fill="none" stroke="var(--lime)" stroke-width="1.6">
        <circle cx="13" cy="13" r="12"/>
        <circle cx="13" cy="13" r="6.5"/>
        <ellipse cx="13" cy="13" rx="3" ry="6.5"/>
        <line x1="6.5" y1="13" x2="19.5" y2="13"/>
      </svg>
      RoccoStitch.com
    </li>
  </ul>

  <div class="company">
    <div class="company__name">ROCCO STITCH INC</div>
    <div>4410 Forge Ridge Ct Ste 7</div>
    <div>Bellmont, CO 80199</div>
  </div>

  <div class="social">
    <span class="social__dot"></span>
    <span>@roccostitch</span>
  </div>

  <div class="tagline-band">
    <span class="tagline-band__lead">Every Logo Has A Story</span>
    <span class="tagline-band__close">Thread Yours</span>
  </div>
</section>

</body>
</html>
```